car wrap design 2019 Vantrel 170WB high roof white color

Im looking for a catchy but simple car wrap design for a van 2019Mercedes Vantrel Van 170 WB . Its a Heating and Cooling company specializing in the residential market. Installation, service and maintenance of all heating and Cooling equipment . Van is white and im looking for a partial wrap with 3 other colours red ,blue and grey. Something simple my name "The Frostline Heating and Cooling " website "thefrostline.ca phone nr "555-314-2087 and logo and description of what im doing . .

Industry/Entity Type

Hvac

Colors

Designer to choose colors to be used in the design.

Requirements
Must have
• big logo see file attached phone nr 555-314-2087 web. thefrostline.ca
Nice to have
• stand out logo visible ,phone nr
Should not have
• too many colours max 4 colours white red blue and maybe gray. no curvy lines

```html
<!DOCTYPE html>
<html lang="en">
<head>
<meta charset="utf-8">
<title>The Frostline Heating and Cooling – Van Wrap</title>
<link rel="stylesheet" href="https://fonts.googleapis.com/css2?family=Russo+One&family=Roboto+Condensed:wght@500;700&family=Open+Sans:wght@400;700&display=swap">
<style>
  :root {
    --wrap-white: #ffffff;
    --body-white: #f4f4f4;
    --outline: #d8d8d8;
    --band-grey: #4b4d52;
    --ink: #2b2b2b;
    --brand-red: #d9281c;
    --brand-orange: #f0641e;
    --brand-amber: #f59a2a;
    --hero-blue: #2f7fd0;
    --hero-orange: #f2a548;
    --page: #ffffff;
  }
  html, body {
    margin: 0;
    padding: 0;
    width: 1200px;
    height: 1200px;
    overflow: hidden;
    background: var(--page);
  }
  .canvas {
    position: relative;
    width: 1200px;
    height: 1200px;
  }
  .panel {
    position: absolute;
    overflow: hidden;
    background: var(--body-white);
    border: 1px solid var(--outline);
    box-sizing: border-box;
  }
  .brand-name {
    position: absolute;
    margin: 0;
    font-family: "Russo One", sans-serif;
    font-weight: 400;
    color: var(--brand-red);
    line-height: 1;
    text-transform: uppercase;
    white-space: nowrap;
  }
  .phone {
    position: absolute;
    margin: 0;
    font-family: "Roboto Condensed", sans-serif;
    font-weight: 700;
    color: var(--ink);
    white-space: nowrap;
  }
  .website {
    position: absolute;
    margin: 0;
    font-family: "Open Sans", sans-serif;
    font-weight: 400;
    color: var(--ink);
    white-space: nowrap;
  }
  .website b { font-weight: 700; }
  .services {
    margin: 0;
    font-family: "Roboto Condensed", sans-serif;
    font-weight: 700;
    text-transform: uppercase;
    color: var(--wrap-white);
  }
  .hero-art {
    position: absolute;
    border-radius: 6px;
  }

  /* Side panel */
  .side-panel {
    left: 31px; top: 106px; width: 1138px; height: 450px;
    border-radius: 60px 24px 18px 18px;
  }
  .side-panel .red-end {
    position: absolute; right: 0; top: 0; width: 300px; height: 340px;
    background: linear-gradient(90deg, var(--brand-orange), var(--brand-red) 60%);
  }
  .side-panel .grey-band {
    position: absolute; left: 0; right: 0; top: 340px; height: 110px;
    background: var(--band-grey);
  }
  .side-panel .services {
    position: absolute; left: 250px; top: 22px; font-size: 17px; letter-spacing: 0.2px;
  }
  .side-panel .brand-name.line-1 { left: 370px; top: 110px; font-size: 50px; }
  .side-panel .brand-name.line-2 { left: 372px; top: 166px; font-size: 29px; }
  .side-panel .phone { left: 198px; top: 274px; font-size: 30px; }
  .side-panel .website { left: 432px; top: 276px; font-size: 26px; letter-spacing: 3px; }
  .side-panel .hero-art {
    left: 820px; top: 20px; width: 290px; height: 380px;
    background: linear-gradient(160deg, var(--hero-blue) 0%, var(--hero-orange) 55%, var(--hero-blue) 100%);
  }

  /* Rear panel */
  .rear-panel {
    left: 181px; top: 662px; width: 350px; height: 440px;
    border-radius: 18px 18px 8px 8px;
    background: linear-gradient(180deg, var(--brand-red) 0%, var(--brand-orange) 70%, var(--brand-amber) 100%);
  }
  .rear-panel .window-field {
    position: absolute; left: 32px; top: 14px; width: 286px; height: 200px;
    background: var(--body-white); border-radius: 10px;
  }
  .rear-panel .hero-art {
    left: 118px; top: 10px; width: 60px; height: 72px;
    background: linear-gradient(160deg, var(--hero-blue), var(--hero-orange));
  }
  .rear-panel .brand-name.line-1 { left: 18px; top: 94px; font-size: 26px; }
  .rear-panel .brand-name.line-2 { left: 22px; top: 124px; font-size: 15px; }
  .rear-panel .phone { left: 60px; top: 158px; font-size: 30px; }
  .rear-panel .website {
    left: 0; width: 350px; text-align: center; top: 220px;
    font-size: 16px; letter-spacing: 2px; color: var(--wrap-white);
  }
  .rear-panel .services {
    position: absolute; left: 40px; width: 270px; top: 300px;
    text-align: center; font-size: 14px; line-height: 1.35;
  }

  /* Front panel */
  .front-panel {
    left: 662px; top: 650px; width: 413px; height: 260px;
    border-radius: 80px 80px 14px 14px;
  }
  .front-panel .hero-art {
    left: 182px; top: 110px; width: 46px; height: 46px;
    background: linear-gradient(160deg, var(--hero-blue), var(--hero-orange));
  }
  .front-panel .brand-name.line-1 { left: 102px; top: 162px; font-size: 21px; }
  .front-panel .brand-name.line-2 { left: 106px; top: 186px; font-size: 12.5px; }
</style>
</head>
<body>
<main class="canvas">

  <section class="panel side-panel" aria-label="Side wrap panel">
    <div class="red-end"></div>
    <div class="hero-art" role="img" aria-label="Mascot illustration: costumed hero in blue and orange running forward"></div>
    <h1 class="brand-name line-1">The Frostline</h1>
    <p class="brand-name line-2">Heating and Cooling</p>
    <p class="phone">555-314-2087</p>
    <p class="website">www.<b>thefrostline</b>.ca</p>
    <div class="grey-band">
      <p class="services">Installation, service and maintenance of all heating and cooling equipment</p>
    </div>
  </section>

  <section class="panel rear-panel" aria-label="Rear wrap panel">
    <div class="window-field">
      <div class="hero-art" role="img" aria-label="Small mascot illustration in blue and orange"></div>
      <p class="brand-name line-1">The Frostline</p>
      <p class="brand-name line-2">Heating and Cooling</p>
      <p class="phone">555-314-2087</p>
    </div>
    <p class="website">www.<b>thefrostline</b>.ca</p>
    <p class="services">Installation, service and maintenance of all heating and cooling equipment</p>
  </section>

  <section class="panel front-panel" aria-label="Front hood panel">
    <div class="hero-art" role="img" aria-label="Small mascot illustration in blue and orange"></div>
    <p class="brand-name line-1">The Frostline</p>
    <p class="brand-name line-2">Heating and Cooling</p>
  </section>

</main>
</body>
</html>
```